Jan 2020 Newsletter

To send out information with some graphical representation to our clients.

Target Market(s)

Property Owners and Managers

Industry/Entity Type

Property

Colors
acd037

Requirements
Must have
• Must have branding
• www.veridelta.co.uk
Nice to have
• Must be information and provide facts and clear guidelines
• you can see other projects that have been done for us.
• Please refer to attachment for the information for the newsletter. This is in Word format
• Please refer to other projects we have posted on here to give an idea of what we have had in the past.

```html
<!DOCTYPE html>
<html lang="en">
<head>
<meta charset="utf-8">
<title>Veridelta – January 2020 Newsletter</title>
<link href="https://fonts.googleapis.com/css2?family=Raleway:wght@400;500;600;700;800&display=swap" rel="stylesheet">
<style>
:root{
  --green:#3dae4a;
  --green-dark:#2a8a35;
  --green-text:#43b649;
  --ink:#333333;
  --grey-band:#3e3e3e;
  --table-head:#3a3a3a;
  --risk-high:#6a6a6a;
  --risk-mid:#8e8e8e;
  --risk-low:#ababab;
  --white:#ffffff;
}
*{margin:0;padding:0;box-sizing:border-box}
html,body{width:1200px;height:4008px;overflow:hidden;background:var(--white)}
body{font-family:'Raleway',sans-serif;color:var(--ink);position:relative}

.masthead{position:absolute;left:0;top:0;width:1200px;height:492px;background:var(--green)}
.masthead::after{content:"";position:absolute;left:576px;bottom:-22px;border-left:24px solid transparent;border-right:24px solid transparent;border-top:22px solid var(--green)}
.brand{position:absolute;left:0;top:50px;width:524px;height:121px;background:var(--white);border-radius:0 61px 61px 0;display:flex;align-items:center;padding-left:68px;gap:16px}
.brand-dot{width:46px;height:46px;border-radius:50%;background:var(--green)}
.brand-name{font-weight:800;font-size:58px;letter-spacing:1px;color:#3a3a3a}
.headline{position:absolute;left:67px;top:190px;color:var(--white);font-weight:700;font-size:58px;line-height:68px;letter-spacing:.5px}
.subhead{position:absolute;left:67px;top:350px;color:var(--white);font-weight:500;font-size:44px;line-height:54px}
.hero-visual{position:absolute;left:708px;top:72px;width:466px;height:395px;border-radius:14px;background:linear-gradient(160deg,#1a2a6e 0%,#2d4bb0 55%,#0f1640 100%)}

.article{position:absolute;left:67px;top:538px;width:1064px;font-size:24px;line-height:30.2px;text-align:justify}
.article p{margin-bottom:30px}

.next-steps{position:absolute;left:0;top:1925px;width:1200px;height:1136px;background:var(--grey-band);color:var(--white);padding:40px 67px 0}
.ribbon{position:relative;margin:0 auto 22px;width:300px;height:56px;background:var(--green);color:var(--white);font-weight:800;font-size:38px;display:flex;align-items:center;justify-content:center}
.ribbon::before,.ribbon::after{content:"";position:absolute;top:0;border-top:28px solid var(--green);border-bottom:28px solid var(--green)}
.ribbon::before{left:-32px;border-left:16px solid transparent;border-right:16px solid var(--green)}
.ribbon::after{right:-32px;border-right:16px solid transparent;border-left:16px solid var(--green)}
.step{font-size:24px;line-height:30.2px;text-align:justify;margin-bottom:34px}
.step strong{color:var(--green-text);font-weight:700;font-size:29px}

.table-title{position:absolute;left:110px;top:3101px;width:980px;height:125px;background:var(--green);color:var(--white);font-weight:800;font-size:35px;line-height:44px;text-align:center;display:flex;align-items:center;justify-content:center}
.table-title::before,.table-title::after{content:"";position:absolute;top:30px;width:0;border-top:56px solid var(--green-dark);border-bottom:56px solid var(--green-dark)}
.table-title::before{left:-48px;border-left:24px solid transparent;border-right:24px solid var(--green-dark);z-index:-1}
.table-title::after{right:-48px;border-right:24px solid transparent;border-left:24px solid var(--green-dark);z-index:-1}

.epc-table{position:absolute;left:78px;top:3278px;width:1045px;border-collapse:collapse;border:3px solid var(--table-head);font-size:24px;text-align:center}
.epc-table th{background:var(--table-head);color:var(--white);font-weight:700;height:59px;border-right:1px solid #777}
.epc-table td{height:60px;font-weight:500;border-right:1px solid #bbb}
.epc-table col.c1,.epc-table col.c2{width:222px}
.epc-table col.c3{width:271px}
.risk{color:var(--white);vertical-align:top;padding-top:16px}
.risk.high{background:var(--risk-high)}
.risk.mid{background:var(--risk-mid)}
.risk.low{background:var(--risk-low)}
.spacer td{height:16px}
.total td{background:var(--table-head);color:var(--white);font-weight:700;height:62px}
.unrated td{height:88px;font-weight:600;border-top:1px solid #bbb}

.footer-band{position:absolute;left:0;top:3968px;width:1200px;height:40px;background:var(--green);color:var(--white);font-weight:700;font-size:22px;line-height:40px;text-align:center;letter-spacing:1px}
</style>
</head>
<body>

<header class="masthead">
  <div class="brand"><span class="brand-name">VERIDELTA</span><span class="brand-dot"></span></div>
  <h1 class="headline">SETTING EPC TARGET<br>TO BAND B,</h1>
  <p class="subhead">Is a start, but there’s still a<br>long way to go</p>
  <div class="hero-visual" role="img" aria-label="Computer screen showing a night view of a lit London bridge"></div>
</header>

<main class="article">
  <p>There has been much taught about whether tightening the minimum energy efficiency standard of EPC to band ‘B’ by 2030 for commercial properties would unlock economic opportunities for low carbon growth. This forms part of the proposals put forward by the government in October and the input into the consultation on the future of the Minimum Energy Efficiency Standards (MEES) on January 7, 2020</p>
  <p>There is a broad agreement that despite the seemingly lack of enforcement, MEES is having a transformational impact in the market and that a minimum EPC band B target by 2030, expected to cover 85 per cent of the privately rented commercial stock, is the right path. However, there is also a broad acknowledgement that in the context of shifting to a net zero economy by 2050, the current framework does not go far enough as it does not target actual operational energy use and therefore, actual carbon emissions.</p>
  <p>Achieving the target EPC band B will, in most cases, require costly strategies which may be difficult to implement depending on the leasing and refurbishment cycles of an asset. The government estimates that to bring existing commercial buildings up to the target EPC band B by 2030 it would cost £50billion.</p>
  <p>Under current exemption rules, energy efficiency improvements will only be required if they are deemed to be cost-effective, so not all buildings will be expected to meet the target. These properties will still be lettable providing that landlords can prove that the highest rating has been achieved. In these cases, introducing the requirement to have a minimum (actual) operational energy rating such as a Display Energy Certificate would be a welcomed move that could incentivise interaction between asset owners and occupants, drive energy performance and reduce emissions.</p>
  <p>Addressing the ‘in-use’ performance of commercial buildings can deliver significant energy and carbon savings, and from our own experience at Halberd &amp; Co we have seen this can be achieved very cost-efficiently.</p>
  <p>For example, the average savings realised on a selection of assets under our management, as part of an advanced data analytics exercise, was 15 per cent, with a ROI of only months. With the support of one of our technical partners, we implemented a combined hardware and software solution that allowed our site teams to uncover opportunities to solve operational issues and improve comfort for occupiers in the areas that really matter.</p>
  <p>Although MEES has promoted the refurbishment of commercial stock with low EPC ratings, it is hard to say whether energy performance in these properties has improved overall. While capital works will be required to improve performance, a lot can be achieved by focusing on the day-to-day operation of buildings – control strategies of HVAC plant, in particular.</p>
  <p>Exemptions related to cost implications will increase as we approach the MEES deadlines, and there is a clear opportunity for the regulations to address operational energy use by creating a link to an operational energy rating. This can have the potential to ultimately improve the resilience of business premises in the UK.</p>
</main>

<section class="next-steps">
  <h2 class="ribbon">NEXT STEP</h2>
  <p class="step"><strong>Prepare an asset schedule</strong> that identifies that EPC status and lease expiry of all properties.</p>
  <p class="step"><strong>Ensure up to date and accurate EPCs have been prepared.</strong> Some of our Clients are taking the opportunity to produce up to date EPCs for their whole portfolio. The majority are identifying and carrying out EPC’s on the priority assets, e.g. lease expiry by end 2020 with either no current EPC or E, F or G rated, and replacing EPC’s where specialist advice has shown that the rating can easily be lifted.We have consistently seen over the last few years that one of the main reasons for poor EPC ratings is the inappropriate use of assumptions and default values in the original EPC assessment and modelling process. In many cases, just redoing the EPC properly is lifting the property out of the F and G classes. Veridelta recently undertook a review of a portfolio where there were 28 F and G units which, had nothing been done, all would have been unlettable in 2018. By simply re running them (with no cap ex at all) VD lifted all but 1 from F and G’s and lifted 7 to a rating. We have seen this across every portfolio we have been involved in – by rerunning EPC’s we see at least 25% of them lifted with no effort whatsoever.</p>
  <p class="step"><strong>Ensure all future EPC’s are carried out by an approved assessor</strong> (we would recommend that this is the same assessor across all your funds) so that data is all in one place for future modelling, which will become increasingly required and methodology is consistent, who will communicate any issues before EPC’s are lodged and ensure defaults are minimal.</p>
  <p class="step"><strong>Decide what EPC provisions need to be included in future lease agreements.</strong> This might include minimum standards for tenant fit out. Other clients are also considering clauses that explicitly require tenants to maintain minimum EPC ratings or that prohibit them for preparing and lodging their own EPCs for the property they are occupying.</p>
  <p class="step"><strong>Finally, start to plan and implement improvement works on the remaining “high risk” EPC’s where ratings have not been improved.</strong> Identify the works required to achieve a minimum D or E rating as soon as possible so that site works can be combined with planned upgrade or refurbishment works wherever possible. This planning however cannot start until the review detailed in 2) above is complete, which from experience can take several months.</p>
</section>

<h2 class="table-title">SAMPLE PORTFOLIO ESTIMATED CURRENT<br>EPC POSITION BASED ON VD ANALYSIS OF SITES</h2>

<table class="epc-table">
  <colgroup><col class="c1"><col class="c2"><col class="c3"><col class="c4"></colgroup>
  <thead><tr><th>EPC RATING</th><th>QUANTITY</th><th>PORTFOLIO %</th><th>RISK %</th></tr></thead>
  <tbody>
    <tr><td>A</td><td>5</td><td>0.17%</td><td class="risk high" rowspan="4">69.94%</td></tr>
    <tr><td>B</td><td>133</td><td>4.64%</td></tr>
    <tr><td>C</td><td>905</td><td>31.56%</td></tr>
    <tr><td>D</td><td>963</td><td>33.58%</td></tr>
    <tr><td>E</td><td>526</td><td>18.34%</td><td class="risk mid">18.34%</td></tr>
    <tr><td>F</td><td>193</td><td>6.73%</td><td class="risk low" rowspan="2">11.72%</td></tr>
    <tr><td>G</td><td>143</td><td>4.99%</td></tr>
    <tr class="spacer"><td></td><td></td><td></td><td></td></tr>
    <tr class="total"><td>TOTAL</td><td>2868</td><td>100%</td><td>100.00%</td></tr>
    <tr class="unrated"><td>NOT RATED</td><td>2303</td><td></td><td></td></tr>
  </tbody>
</table>

<footer class="footer-band">www.veridelta.co.uk</footer>

</body>
</html>
```